KORIVA iOS App needs a cool consumer marketing page

KORIVA is an iOS app for getting files onto your iOS device. We have an app in the Plumtree store and we're about to launch version 2. We have a strong theme already with characters appearing in the app (you can see screen shots on www.koriva-example.com). The existing website is from a simple template - we want a site that shows off the app, steps people through what the app can do, and should look quirky, not corporate. We want to keep the existing icon/logo.

There's a matching iOS interface brief here: http://jobs.example-gigboard.com/job.aspx?id=738215
Updates

Some additional information, this is a non-coding brief.

We'd like to keep the existing theme that matches the name KORIVA - slightly Japanese / far east , sophisticated young consumer with a grasp of technology.  We need to convey feature set, screen shots of the app, pricing, FAQs, a contact / invite form.

Thanks, and we're looking forward to your contributions.

Thank you for some great designs so far.  Can you also tell me how you think these pages would be presented.  I'm not looking for code, but would these be parallax scrolled section for example?  Using something like glidrix?  If so, these sort of pages normally have quite big backgrounds, what would you suggest?

Thanks.

Target Market(s)

Young, techno savvy consumers

Industry/Entity Type

Marketing

Font styles to use
Sans Serif

```html
<!DOCTYPE html>
<html lang="en">
<head>
<meta charset="utf-8">
<title>KORIVA – Newsletter &amp; Pricing</title>
<link rel="stylesheet" href="https://fonts.googleapis.com/css2?family=Arimo:wght@400;700&family=Quicksand:wght@500;700&display=swap">
<style>
:root{
  --page-bg:#f2f2f2;
  --band-bg:#52b8e3;
  --text-muted:#8c8c8c;
  --heading-grey:#8a8a8a;
  --go-green:#52d96a;
  --white:#ffffff;
  --row-line:#d9d9d9;
  --row-text:#8e8e8e;
  --badge-black:#111111;

  --basic-green-head:#47c43a;
  --basic-green-body:#7cd36f;
  --basic-green-btn:#5ccc5a;
  --basic-teal-head:#409f9c;
  --basic-teal-body:#73d3d1;
  --basic-teal-btn:#5bc3c1;
  --premium-head:#15709c;
  --premium-body:#1c8bbf;
  --premium-btn:#2aa8e2;
  --pro-purple-head:#9274c0;
  --pro-purple-body:#a987e0;
  --pro-purple-btn:#9a78d5;
  --pro-orange-head:#ec8c1d;
  --pro-orange-body:#fca843;
  --pro-orange-btn:#f6952d;
}
*{box-sizing:border-box;margin:0;padding:0}
html,body{width:1200px;height:900px;overflow:hidden}
body{background:var(--page-bg);font-family:"Arimo",Arial,sans-serif;position:relative}

.newsletter{position:absolute;left:0;top:0;width:1200px;height:388px}
.newsletter-icon{position:absolute;left:217px;top:30px}
.newsletter-title{position:absolute;left:262px;top:28px;font-family:"Quicksand",sans-serif;font-weight:700;font-size:21px;letter-spacing:1.45px;color:var(--heading-grey)}
.newsletter-lead{position:absolute;left:262px;top:64px;font-size:12px;color:var(--text-muted)}
.email-field{position:absolute;left:263px;top:102px;width:317px;height:33px;background:var(--white);border:1px solid #cfcfcf;font-family:"Quicksand",sans-serif;font-size:14px;letter-spacing:.6px;color:#8a8a8a;padding:7px 12px}
.go-button{position:absolute;z-index:2;left:595px;top:102px;width:70px;height:32px;background:var(--go-green);color:var(--white);font-family:"Quicksand",sans-serif;font-weight:700;font-size:14px;letter-spacing:2px;text-align:center;line-height:32px}
.app-screens{position:absolute;z-index:1;left:550px;top:95px;width:380px;height:285px;
  background:radial-gradient(ellipse 55% 12% at 50% 92%,rgba(0,0,0,.16),rgba(0,0,0,0) 100%),
  linear-gradient(115deg,rgba(255,255,255,0) 0%,#ffffff 18%,#f4f4f4 60%,#d6d6d6 88%,rgba(242,242,242,0) 100%);
  clip-path:polygon(0 82%,22% 0,100% 5%,78% 100%)}

.pricing{position:absolute;left:0;top:388px;width:1200px;height:390px;background:var(--band-bg)}
.store-badge{position:absolute;left:537px;top:31px;width:138px;height:39px;background:var(--badge-black);border:1px solid #6d6d6d;border-radius:6px}

.plan{position:absolute;top:93px;width:170px;height:264px;color:var(--white)}
.plan-name{height:39px;text-align:center;font-weight:700;font-size:20px;line-height:39px}
.plan-price{height:52px;padding-left:23px;padding-top:14px;white-space:nowrap}
.plan-price .currency{font-size:17px;vertical-align:top;position:relative;top:-3px}
.plan-price .amount{font-size:25px;font-weight:700;margin-left:6px}
.plan-price .period{font-size:13px;margin-left:12px}
.plan-features{position:absolute;left:5px;top:91px;width:160px;height:150px;background:var(--white);list-style:none;padding:0 8px 0 7px}
.plan-features li{height:27px;border-bottom:1px solid var(--row-line);font-size:11px;color:var(--row-text);line-height:18px;padding-left:3px;padding-top:6px}
.plan-features li:first-child{height:32px;padding-top:9px}
.buy-button{position:absolute;left:50px;top:229px;width:70px;height:24px;border-radius:2px;text-align:center;font-weight:700;font-size:13px;line-height:24px;color:var(--white);box-shadow:0 2px 0 rgba(0,0,0,.12)}

.plan-basic-green{left:127px;background:var(--basic-green-body)}
.plan-basic-green .plan-name{background:var(--basic-green-head)}
.plan-basic-green .buy-button{background:var(--basic-green-btn)}
.plan-basic-teal{left:330px;background:var(--basic-teal-body)}
.plan-basic-teal .plan-name{background:var(--basic-teal-head)}
.plan-basic-teal .buy-button{background:var(--basic-teal-btn)}
.plan-premium{left:523px;background:var(--premium-body)}
.plan-premium .plan-name{background:var(--premium-head)}
.plan-premium .buy-button{background:var(--premium-btn)}
.plan-premium .plan-price .period{margin-left:4px}
.plan-pro-purple{left:723px;background:var(--pro-purple-body)}
.plan-pro-purple .plan-name{background:var(--pro-purple-head)}
.plan-pro-purple .buy-button{background:var(--pro-purple-btn)}
.plan-pro-orange{left:918px;background:var(--pro-orange-body)}
.plan-pro-orange .plan-name{background:var(--pro-orange-head)}
.plan-pro-orange .buy-button{background:var(--pro-orange-btn)}
</style>
</head>
<body>

<section class="newsletter">
  <svg class="newsletter-icon" width="35" height="23" viewBox="0 0 35 23" fill="none" stroke="#9a9a9a" stroke-width="1.6">
    <rect x="1" y="1" width="33" height="21"/>
    <polyline points="1,1 17.5,13 34,1"/>
    <line x1="1" y1="22" x2="13" y2="10"/>
    <line x1="34" y1="22" x2="22" y2="10"/>
  </svg>
  <h2 class="newsletter-title">SUBSCRIBE TO OUR NEWSLETTER</h2>
  <p class="newsletter-lead">Stay up to date with our latest developments.</p>
  <div class="email-field">Your@inbox.example</div>
  <div class="go-button">GO</div>
  <div class="app-screens" role="img" aria-label="Three KORIVA app screens tilted in perspective: cloud provider choice, notification settings and upload expiry slider, with the app's character"></div>
</section>

<section class="pricing">
  <div class="store-badge" role="img" aria-label="Plumtree store download badge"></div>

  <div class="plan plan-basic-green">
    <div class="plan-name">BASIC</div>
    <div class="plan-price"><span class="currency">$</span><span class="amount">3.99</span><span class="period">/ month</span></div>
    <ul class="plan-features"><li>Lorem Ipsum</li><li>Lorem Ipsum</li><li>Lorem Ipsum</li><li>Lorem Ipsum</li></ul>
    <div class="buy-button">BUY</div>
  </div>

  <div class="plan plan-basic-teal">
    <div class="plan-name">BASIC</div>
    <div class="plan-price"><span class="currency">$</span><span class="amount">3.99</span><span class="period">/ month</span></div>
    <ul class="plan-features"><li>Lorem Ipsum</li><li>Lorem Ipsum</li><li>Lorem Ipsum</li><li>Lorem Ipsum</li></ul>
    <div class="buy-button">BUY</div>
  </div>

  <div class="plan plan-premium">
    <div class="plan-name">PREMIUM</div>
    <div class="plan-price"><span class="currency">$</span><span class="amount">14.99</span><span class="period">/ month</span></div>
    <ul class="plan-features"><li>Lorem Ipsum</li><li>Lorem Ipsum</li><li>Lorem Ipsum</li><li>Lorem Ipsum</li></ul>
    <div class="buy-button">BUY</div>
  </div>

  <div class="plan plan-pro-purple">
    <div class="plan-name">PRO</div>
    <div class="plan-price"><span class="currency">$</span><span class="amount">7.99</span><span class="period">/ month</span></div>
    <ul class="plan-features"><li>Lorem Ipsum</li><li>Lorem Ipsum</li><li>Lorem Ipsum</li><li>Lorem Ipsum</li></ul>
    <div class="buy-button">BUY</div>
  </div>

  <div class="plan plan-pro-orange">
    <div class="plan-name">PRO</div>
    <div class="plan-price"><span class="currency">$</span><span class="amount">7.99</span><span class="period">/ month</span></div>
    <ul class="plan-features"><li>Lorem Ipsum</li><li>Lorem Ipsum</li><li>Lorem Ipsum</li><li>Lorem Ipsum</li></ul>
    <div class="buy-button">BUY</div>
  </div>
</section>

</body>
</html>
```